Non-profit organisation for street children in Indonesia

Lentera Bocah provides home, education, family and health care for street children and other underprivileged children in Indonesia.

We need an emotional catchy advertisement that will make people aware of the terrible living conditions of street children in Indonesia and the great work the Lentera Bocah Foundation is doing to help these children.

We have 1 photo available for this advertisement. A little girl laying in the streets. This photo can be used with a strong quote such as "Street children whose responsibility?" or "Safer out on streets than at home" or "This child doesn't have the right to have a childhood worth remembering?" or another strong quote. Be creative! It need to touch people!

See some similar advertisements of other non-profit organizations what we very much like:

http://7brightpix.example/wp-content/uploads/2011/07/boldposters41.jpg
http://7brightpix.example/wp-content/uploads/2011/07/affiches-nobles-motifs-058.jpg

Mission
To give every child in the world the opportunity to live a happy and healthy life free of poverty, exploitation, and violence.

Overview
Lentera Bocah Foundation is an independent non-governmental organisation founded in 2005 in the Netherlands and expanded to Indonesia in 2006. Our aim is to improve the lives of children and to protect their rights by providing education, accommodation, family care and medical and legal aid.

Description
Lentera Bocah (Light for Youngsters) Foundation serves homeless and impoverished children by offering them a new path in life. By providing them with the necessary shelter, education, and psychological support directed towards vocational training, mentorship, and micro-credit opportunities, it strives to enable their re-entery into the community as happy and self-sufficient adults.

Facts:
There are 70 million children in Indonesia, nearly 18 million are very poor and estimated 170,000 children live on the streets.

Pitch submissions need to be 960x696 pixels.

Files available 1 photo and logo
Updates

Reason: Dear Designers, We have decided to extend the deadline because we haven't received what we are after. Please make a design in the trend as the following two examples: http://7brightpix.example/wp-content/uploads/2011/07/boldposters41.jpg http://7brightpix.example/wp-content/uploads/2011/07/affiches-nobles-motifs-058.jpg We hope to receive a good design shortly! Thank you Kind regards Lentera Bocah

Target Market(s)

Everybody

Industry/Entity Type

Non-Profit

Requirements
Must have
• 1. A strong quote.
2. Website url: www.lenterabocah.org
3. Mission quote from Lentera Bocah:
Should not have
• To much text.

```html
<!DOCTYPE html>
<html lang="en">
<head>
<meta charset="utf-8">
<title>Lentera Bocah – Street children whose responsibility?</title>
<link rel="stylesheet" href="https://fonts.googleapis.com/css2?family=Montserrat:ital,wght@0,300;0,400;0,700;1,700&display=swap">
<style>
  :root {
    --page-bg: #ffffff;
    --asphalt-dark: #3a3a3a;
    --asphalt-mid: #5e5e5e;
    --pavement-light: #8a8a8a;
    --headline: #ffffff;
    --bar-bg: #000000;
    --mission-green: #1f8a1f;
    --donate-green: #2f9a2f;
    --bar-text: #ffffff;
    --brand-yellow: #f2e21b;
    --url-yellow: #e8b400;
  }
  * { margin: 0; padding: 0; box-sizing: border-box; }
  html, body {
    width: 1200px;
    height: 1100px;
    overflow: hidden;
    background: var(--page-bg);
    font-family: "Montserrat", Arial, sans-serif;
  }
  .poster {
    position: absolute;
    left: 123px;
    top: 92px;
    width: 960px;
    height: 696px;
    overflow: hidden;
  }
  .street-photo {
    position: absolute;
    inset: 0;
    background:
      radial-gradient(ellipse 260px 120px at 560px 390px, rgba(190,70,50,0.55), rgba(190,70,50,0) 70%),
      linear-gradient(160deg, var(--asphalt-mid) 0%, var(--asphalt-dark) 45%, var(--pavement-light) 100%);
  }
  .headline {
    position: absolute;
    left: 32px;
    top: 204px;
    color: var(--headline);
    font-weight: 300;
    white-space: nowrap;
    line-height: 1;
  }
  .headline-lead { font-size: 26px; letter-spacing: 0.2px; }
  .headline-key { font-size: 83px; letter-spacing: -1.5px; margin-left: 8px; }
  .brand {
    position: absolute;
    left: 40px;
    top: 616px;
    display: flex;
    align-items: center;
    gap: 10px;
  }
  .brand-name {
    color: var(--brand-yellow);
    font-weight: 700;
    font-size: 19px;
    line-height: 1.1;
    width: 140px;
  }
  .brand-dot {
    width: 26px;
    height: 26px;
    border-radius: 50%;
    background: var(--brand-yellow);
  }
  .info-bar {
    position: absolute;
    left: 241px;
    top: 608px;
    width: 618px;
    height: 62px;
    background: var(--bar-bg);
    display: flex;
    align-items: center;
    overflow: hidden;
  }
  .mission {
    width: 270px;
    flex: none;
    padding-left: 13px;
    color: var(--mission-green);
    font-style: italic;
    font-weight: 700;
    font-size: 9.5px;
    line-height: 13px;
    white-space: nowrap;
  }
  .divider {
    flex: none;
    width: 1px;
    height: 34px;
    background: var(--bar-text);
    margin: 0 14px 0 0;
  }
  .donate {
    color: var(--bar-text);
    font-size: 9.5px;
    line-height: 13px;
    letter-spacing: -0.1px;
    white-space: nowrap;
  }
  .donate-word {
    color: var(--donate-green);
    font-size: 17px;
    letter-spacing: 0.2px;
  }
  .url-name { color: var(--url-yellow); }
</style>
</head>
<body>
  <main class="poster">
    <div class="street-photo" role="img" aria-label="Black and white photo of a curving city street with a little girl in red trousers lying face down on the kerb"></div>

    <h1 class="headline">
      <span class="headline-lead">Street children whose</span><span class="headline-key">responsibility?</span>
    </h1>

    <div class="brand">
      <span class="brand-name">Lentera Bocah Foundation</span>
      <span class="brand-dot"></span>
    </div>

    <div class="info-bar">
      <p class="mission">"Our vision is to give every child in the world<br>the opportunity to live a happy and healthy life<br>free of poverty, exploitation and violence."</p>
      <span class="divider"></span>
      <p class="donate"><span class="donate-word">DONATE</span> to GIRO 4732 t.a.v. Stichting Lentera Bocah or<br>financial adopt a child on www.<span class="url-name">lenterabocah</span>.org</p>
    </div>
  </main>
</body>
</html>
```